Business Card Design

Consultant ot credit unions that operate a property and casualty insurance agency

Industry/Entity Type

Insurance

Contact Information for Business Card

Dorian Velker
Harborline Cover Agency Consultant
dorianvelker@mailvoro.com
562 318-4092
914 Tamsin Court
Long Beach, CA 90813

```html
<!DOCTYPE html>
<html lang="en">
<head>
<meta charset="utf-8">
<title>Harborline Cover – Business Card</title>
<link rel="stylesheet" href="https://fonts.googleapis.com/css2?family=Open+Sans:wght@400;700&display=swap">
<style>
  :root {
    --backdrop: #e6e7e9;
    --sky: #8fd6f6;
    --ocean: #22a3df;
    --navy: #2a3a4d;
    --white: #ffffff;
  }
  * { margin: 0; padding: 0; box-sizing: border-box; }
  html, body { width: 1200px; height: 856px; overflow: hidden; }
  body {
    background: var(--backdrop);
    font-family: "Open Sans", Arial, sans-serif;
    position: relative;
  }
  .card {
    position: absolute;
    left: 150px;
    top: 171px;
    width: 900px;
    height: 514px;
    border-radius: 44px;
    overflow: hidden;
    background: var(--sky);
    box-shadow: 0 6px 24px rgba(0,0,0,0.12);
  }
  .card-art { position: absolute; inset: 0; }
  .brand {
    position: absolute;
    left: 170px;
    top: 110px;
    display: flex;
    align-items: center;
    gap: 18px;
    color: var(--navy);
  }
  .brand-mark {
    width: 62px;
    height: 62px;
    border-radius: 50%;
    background: var(--navy);
  }
  .brand-name {
    font-weight: 700;
    font-size: 40px;
    letter-spacing: 2px;
    line-height: 1;
  }
  .holder {
    position: absolute;
    left: 60px;
    top: 392px;
    color: var(--navy);
  }
  .holder-name {
    font-size: 27px;
    font-weight: 400;
    text-decoration: underline;
    text-underline-offset: 4px;
    text-decoration-thickness: 2px;
  }
  .holder-role {
    color: var(--white);
    font-size: 24px;
    margin-top: 2px;
  }
  .contact {
    position: absolute;
    left: 560px;
    top: 262px;
    list-style: none;
    color: var(--navy);
    font-size: 18px;
    line-height: 1.25;
  }
  .contact-item {
    display: flex;
    align-items: flex-start;
    gap: 14px;
    margin-bottom: 12px;
  }
  .contact-icon { flex: none; width: 30px; height: 30px; }
</style>
</head>
<body>
  <main class="card">
    <svg class="card-art" width="900" height="514" viewBox="0 0 900 514" aria-hidden="true">
      <polygon class="lower-band" points="0,360 900,145 900,514 0,514" fill="#22a3df"/>
      <line class="divider" x1="0" y1="358" x2="900" y2="143" stroke="#2a3a4d" stroke-width="8"/>
    </svg>

    <div class="brand">
      <span class="brand-mark"></span>
      <span class="brand-name">HARBORLINE COVER</span>
    </div>

    <div class="holder">
      <p class="holder-name">Dorian Velker</p>
      <p class="holder-role">Agency Consultant</p>
    </div>

    <ul class="contact">
      <li class="contact-item">
        <svg class="contact-icon" viewBox="-15 -15 30 30" aria-hidden="true">
          <circle r="15" fill="#2a3a4d"/>
          <path d="M-5,-6 l3,-1 2,4 -2,1.5 q1.5,3 4,4 l1.5,-2 4,2 -1,3 q-6,1 -11.5,-11.5z" fill="#fff"/>
        </svg>
        <span>562 318-4092</span>
      </li>
      <li class="contact-item">
        <svg class="contact-icon" viewBox="-15 -15 30 30" aria-hidden="true">
          <circle r="15" fill="#2a3a4d"/>
          <rect x="-7" y="-5" width="14" height="10" fill="#fff"/>
          <path d="M-7,-5 L0,1 L7,-5" fill="none" stroke="#2a3a4d" stroke-width="1.3"/>
        </svg>
        <span>dorianvelker@mailvoro.com</span>
      </li>
      <li class="contact-item">
        <svg class="contact-icon" viewBox="-15 -15 30 30" aria-hidden="true">
          <circle r="15" fill="#2a3a4d"/>
          <path d="M-7,0 L0,-7 L7,0 L5,0 L5,6 L1.5,6 L1.5,2 L-1.5,2 L-1.5,6 L-5,6 L-5,0z" fill="#fff"/>
        </svg>
        <span>914 Tamsin Court Long Beach,<br>CA 90813</span>
      </li>
    </ul>
  </main>
</body>
</html>
```